Blue Heron Journeys

We are a predominantly online travel agency with high-end (first/business class) clients. I'm looking to either have our existing logo revamped or a new logo created with business card layout. I prefer to work with existing logo if possible so it remains familiar with existing clientele. I have uploaded a yellow business card layout showing icons on one side of the card. I would like to keep my existing colours, not yellow. could the company name/tag line go over the icons?
Contact Information for Business Card
Colleen Fairbank
Director
(G.T.L.C. 07815364)
(Quorvanel Pty. Ltd) ABN 61 507 314 829
512/48 Tillbrook Street
Calder Heights | NSW 2468 | Australia
www.blueheronjourneys-example.com.au
m: + 61 (0) 491 738 052
t: + 61 (0) 2 9175 3816
e: colleen@blueheronjourneys-example.com.au

```html
<!DOCTYPE html>
<html lang="en">
<head>
<meta charset="utf-8">
<title>Blue Heron Journeys – Business Card</title>
<link rel="stylesheet" href="https://fonts.googleapis.com/css2?family=Roboto:wght@400;500;700&display=swap">
<style>
  :root {
    --backdrop: #2b2b2b;
    --card: #f5f1ea;
    --mark-panel: #fcfaf6;
    --mark-panel-faint: #f9f6f0;
    --ink: #111111;
    --ink-soft: #4a4a4a;
    --rule: #222222;
  }
  * { margin: 0; padding: 0; box-sizing: border-box; }
  html, body {
    width: 1200px; height: 960px; overflow: hidden;
    background: var(--backdrop);
    font-family: "Roboto", Arial, sans-serif;
  }
  .canvas { position: relative; width: 1200px; height: 960px; }
  .card {
    position: absolute; width: 600px; height: 343px;
    background: var(--card);
  }
  .card--front { left: 314px; top: 113px; }
  .card--back  { left: 311px; top: 472px; }

  .brand-panel {
    position: absolute; left: 310px; top: 45px; width: 255px; height: 99px;
    background: var(--mark-panel);
  }
  .brand-name {
    position: absolute; color: var(--ink); font-weight: 400;
    white-space: nowrap; transform: translateX(-50%);
  }
  .card--front .brand-name { left: 437px; top: 80px; font-size: 22px; }

  .accent-bar {
    position: absolute; left: 0; top: 165px; width: 12px; height: 40px;
    background: var(--ink);
  }
  .person-name {
    position: absolute; left: 39px; top: 162px;
    font-size: 20px; font-weight: 500; color: var(--ink); letter-spacing: .2px;
  }
  .title-row {
    position: absolute; left: 38px; top: 189px; width: 526px;
    display: flex; align-items: center; gap: 4px;
  }
  .person-title { font-size: 14.5px; color: var(--ink-soft); white-space: nowrap; }
  .title-rule { flex: 1; height: 2px; background: var(--rule); margin-top: 4px; }

  .contact-list {
    position: absolute; left: 34px; top: 225px; list-style: none;
    font-size: 13px; color: var(--ink-soft); line-height: 19px; white-space: nowrap;
  }
  .contact-list li { display: flex; align-items: center; gap: 8px; }
  .contact-list svg { width: 13px; height: 13px; fill: var(--ink); flex: none; }
  .contact-list strong { color: var(--ink); font-weight: 700; }
  .details {
    position: absolute; right: 36px; top: 225px; text-align: right;
    font-size: 12px; color: var(--ink-soft); line-height: 19px;
    font-style: normal; white-space: nowrap;
  }

  .card--back .brand-panel {
    left: 164px; top: 128px; width: 280px; height: 135px;
    background: var(--mark-panel-faint);
  }
  .card--back .brand-name { left: 300px; top: 172px; font-size: 32px; }
</style>
</head>
<body>
<main class="canvas">
  <section class="card card--front" aria-label="Business card front">
    <div class="brand-panel" role="img" aria-label="Striped background behind company name"></div>
    <div class="brand-name">Blue Heron Journeys</div>

    <div class="accent-bar"></div>
    <h1 class="person-name">COLLEEN FAIRBANK</h1>
    <div class="title-row">
      <p class="person-title">DIRECTOR</p>
      <div class="title-rule"></div>
    </div>

    <ul class="contact-list">
      <li><svg viewBox="0 0 16 16" aria-hidden="true"><path d="M3 1h3l1.5 4-2 1.3a9 9 0 0 0 4.2 4.2L11 8.5l4 1.5v3a2 2 0 0 1-2 2A12 12 0 0 1 1 3a2 2 0 0 1 2-2z"/></svg>+ 61 (0) 2 9175 3816</li>
      <li><svg viewBox="0 0 16 16" aria-hidden="true"><path d="M4 0h8v16H4zM5.5 2v10h5V2zM7 13.3h2v1.4H7z" fill-rule="evenodd"/></svg>+ 61 (0) 491 738 052</li>
      <li><svg viewBox="0 0 16 16" aria-hidden="true"><path d="M8 1a7 7 0 1 0 0 14A7 7 0 0 0 8 1zm0 1.5a5.5 5.5 0 1 1 0 11 5.5 5.5 0 0 1 0-11zM2.5 7.4h11v1.2h-11zM7.4 2.5h1.2v11H7.4z" fill-rule="evenodd"/></svg>www.<strong>blueheronjourneys-example</strong>.com.au</li>
      <li><svg viewBox="0 0 16 16" aria-hidden="true"><path d="M1 4h14v9H1z"/><path d="M1 4l7 5 7-5" fill="none" stroke="#f5f1ea" stroke-width="1.2"/></svg>colleen@blueheronjourneys-example.com.au</li>
    </ul>

    <address class="details">
      512/48 Tillbrook Street<br>
      Calder Heights | NSW 2468 | Australia<br>
      G.T.L.C. 07815364<br>
      Quorvanel Pty. Ltd ABN 61 507 314 829
    </address>
  </section>

  <section class="card card--back" aria-label="Business card back">
    <div class="brand-panel" role="img" aria-label="Faint striped background behind company name"></div>
    <div class="brand-name">Blue Heron Journeys</div>
  </section>
</main>
</body>
</html>
```